Bref créative
Fire sprinkler company stationary
Halbrook Automatic Sprinkler Co.
Simple
Trent Okafor
President
2745 Pelling Street, Knoxville, TN 37921
contact@halbrooksprinkler.example
The logo to use on the stationary.

```html
<!DOCTYPE html>
<html lang="en">
<head>
<meta charset="utf-8">
<title>Halbrook Automatic Sprinkler Co. — Business Cards</title>
<link href="https://fonts.googleapis.com/css2?family=Archivo+Black&family=Roboto+Condensed:wght@400;700&display=swap" rel="stylesheet">
<style>
  :root {
    --bg: #e9e9ea;
    --card: #ffffff;
    --ink: #111111;
    --black: #0d0d0d;
    --gold: #c9961a;
    --gold-light: #f0c64a;
    --grey: #7a7a7a;
    --white: #ffffff;
  }
  * { margin: 0; padding: 0; box-sizing: border-box; }
  html, body { width: 1200px; height: 1009px; overflow: hidden; }
  body {
    background: var(--bg);
    font-family: "Roboto Condensed", Arial, sans-serif;
    display: flex;
    align-items: center;
    justify-content: center;
    gap: 60px;
  }
  .card {
    position: relative;
    width: 540px;
    height: 309px;
    border-radius: 18px;
    background: var(--card);
    overflow: hidden;
    box-shadow: 0 6px 18px rgba(0,0,0,0.18);
  }
  .card-art { position: absolute; inset: 0; }

  /* front */
  .contact {
    position: absolute;
    left: 22px;
    top: 66px;
    list-style: none;
    color: var(--white);
    font-size: 10px;
    line-height: 1.8;
    letter-spacing: 0.03em;
  }
  .contact li { display: flex; align-items: center; gap: 7px; white-space: nowrap; }
  .contact svg { width: 10px; height: 10px; flex: none; }
  .contact .indent { padding-left: 17px; }
  .brand {
    position: absolute;
    display: flex;
    align-items: center;
    gap: 12px;
  }
  .front .brand { left: 278px; top: 92px; }
  .brand-mark {
    width: 50px; height: 50px;
    border-radius: 50%;
    background: var(--ink);
    flex: none;
  }
  .brand-name {
    font-family: "Archivo Black", Arial, sans-serif;
    font-size: 27px;
    line-height: 1;
    color: var(--ink);
    letter-spacing: 0.01em;
  }
  .brand-tag {
    font-family: "Roboto Condensed", Arial, sans-serif;
    font-weight: 700;
    font-size: 12.5px;
    color: var(--gold);
    letter-spacing: 0.05em;
    margin-top: 4px;
  }
  .person {
    position: absolute;
    right: 26px;
    bottom: 20px;
    text-align: right;
    color: var(--white);
  }
  .person-name { font-size: 14px; font-weight: 700; letter-spacing: 0.05em; }
  .person-title { font-size: 10px; letter-spacing: 0.12em; text-transform: uppercase; color: #cfcfcf; }

  /* back */
  .back .logo-block {
    position: absolute;
    left: 0; right: 0; top: 92px;
    display: flex;
    flex-direction: column;
    align-items: center;
    gap: 10px;
  }
  .back .brand-mark { width: 84px; height: 84px; }
  .back .brand-word {
    font-family: "Archivo Black", Arial, sans-serif;
    font-size: 18px;
    color: var(--ink);
    letter-spacing: 0.04em;
  }
  .website {
    position: absolute;
    left: 0; right: 0; bottom: 44px;
    text-align: center;
    font-size: 12px;
    letter-spacing: 0.32em;
    color: var(--grey);
    text-transform: uppercase;
  }
  .website span { color: var(--gold); }
</style>
</head>
<body>

  <section class="card front" aria-label="Business card front">
    <svg class="card-art" viewBox="0 0 540 309" preserveAspectRatio="none" aria-hidden="true">
      <defs>
        <linearGradient id="goldBand" x1="0" y1="0" x2="1" y2="1">
          <stop offset="0" stop-color="#f0c64a"/>
          <stop offset="0.5" stop-color="#c9961a"/>
          <stop offset="1" stop-color="#8a6410"/>
        </linearGradient>
      </defs>
      <path d="M0 0 H200 C185 120 270 230 540 250 V309 H0 Z" fill="#0d0d0d"/>
      <path d="M200 0 H216 C202 118 286 218 540 232 V250 C270 230 185 120 200 0 Z" fill="url(#goldBand)"/>
      <path d="M224 0 H229 C216 112 300 208 540 222 V226 C294 212 210 116 224 0 Z" fill="#c9961a"/>
    </svg>

    <ul class="contact">
      <li>
        <svg viewBox="0 0 12 12"><path d="M6 0.5a3.8 3.8 0 0 0-3.8 3.8C2.2 7.2 6 11.5 6 11.5s3.8-4.3 3.8-7.2A3.8 3.8 0 0 0 6 0.5Zm0 5.2a1.4 1.4 0 1 1 0-2.8 1.4 1.4 0 0 1 0 2.8Z" fill="#c9961a"/></svg>
        2745 Pelling Street
      </li>
      <li class="indent">Knoxville, TN 37921</li>
      <li>
        <svg viewBox="0 0 12 12"><path d="M2.6 0.8l1.8 0.1 0.9 2.6-1.3 1c0.6 1.3 1.7 2.4 3 3l1-1.3 2.6 0.9 0.1 1.8c-0.3 0.9-1.1 1.5-2 1.4C4.9 10 2 7.1 1.7 3.3c-0.1-1 0.5-2.2 0.9-2.5Z" fill="#c9961a"/></svg>
        (865) 555-0142
      </li>
      <li>
        <svg viewBox="0 0 12 12"><rect x="0.5" y="2" width="11" height="8" rx="1" fill="#c9961a"/><path d="M1 2.6 6 6.5l5-3.9" stroke="#0d0d0d" stroke-width="1" fill="none"/></svg>
        contact@halbrooksprinkler.example
      </li>
      <li>
        <svg viewBox="0 0 12 12"><circle cx="6" cy="6" r="5" fill="none" stroke="#c9961a" stroke-width="1.2"/><path d="M1 6h10M6 1c2 2.5 2 7.5 0 10M6 1c-2 2.5-2 7.5 0 10" stroke="#c9961a" stroke-width="0.9" fill="none"/></svg>
        halbrooksprinkler.example
      </li>
    </ul>

    <div class="brand">
      <div class="brand-mark" role="img" aria-label="Halbrook logo"></div>
      <div>
        <div class="brand-name">HALBROOK</div>
        <div class="brand-tag">AUTOMATIC SPRINKLER CO.</div>
      </div>
    </div>

    <div class="person">
      <div class="person-name">Trent Okafor</div>
      <div class="person-title">President</div>
    </div>
  </section>

  <section class="card back" aria-label="Business card back">
    <div class="logo-block">
      <div class="brand-mark" role="img" aria-label="Halbrook logo"></div>
      <div class="brand-word">HALBROOK</div>
    </div>
    <p class="website">www.<span>halbrooksprinkler</span>.example</p>
  </section>

</body>
</html>
```